Art Wall - Illustrates "Be Colorful"

I have a seasonal color business called Willow Gate Blooms. We plant containers and add colorful annuals to garden beds. I need a 6' tall by 18' long banner that will be hung on a wall or possibly used on the side of my enclosed trailer. The banner will be used as backdrop for ladies taking pictures together and as a backdrop for colorful container gardens to be photographed for our website. It should have the words "Be Colorful" on it. I would like for it to look like a fun art wall that you would take a picture in front of in a downtown area. The art should work well with our logo. We love flowers but other ideas are welcome. Feel free to look at our instagram @willowgatebloomsokc to see examples of our work. I have uploaded our logo and a colorful flower picture we liked (great colors) but didn't quite work with our logo and a fun colorful wall at a restaurant that we really like.

Target Market(s)

women ages 30-45, wealthy, like to feel like they are trendy

Industry/Entity Type

Landscape Gardening

Font styles to use
Serif

Requirements
Must have
• The words "Be Colorful" on it and some space that would good for people to stand or objects to be placed to be photographed.
Nice to have
• We really like the colors in the "sun and skip" t-shirt picture I have attached. Also like the watercolor, alcohol ink, or hand-painted look.
Should not have
• Please do not include our logo on the banner. It will be added as a watermark to our photos.

Please do not literally use the logo flower in the design. Feel free to use pieces or inspiration from the logo but the wall should look more like art and less like a cartoon.

```html
<!DOCTYPE html>
<html lang="en">
<head>
<meta charset="utf-8">
<title>Be Colorful – Willow Gate Blooms Art Wall</title>
<link rel="stylesheet" href="https://fonts.googleapis.com/css2?family=Abril+Fatface&display=swap">
<style>
  :root {
    --paper: #ffffff;
    --burst-blue: #8fb0e0;
    --burst-violet: #7f7fd0;
    --burst-orange: #f2a43c;
    --burst-red: #e2552e;
    --burst-green: #b6cf5a;
    --burst-pink: #e7a8c4;
    --ink-shadow: #1f1d1a;
    --be-gold: #d6a052;
    --col-olive: #6b6650;
    --col-blush: #e2cfc0;
    --col-terracotta: #d86a4e;
    --col-stone: #b9b1a8;
    --col-slate: #7a7d78;
  }
  html, body {
    margin: 0;
    padding: 0;
    width: 1200px;
    height: 403px;
    overflow: hidden;
    background: var(--paper);
  }
  .art-wall {
    position: relative;
    width: 1200px;
    height: 403px;
    overflow: hidden;
    background: var(--paper);
  }
  .watercolor-bursts {
    position: absolute;
    inset: 0;
    background: radial-gradient(ellipse 300px 190px at 50% 50%,
      var(--paper) 0%,
      var(--paper) 45%,
      var(--burst-pink) 62%,
      var(--burst-blue) 75%,
      var(--burst-green) 86%,
      var(--burst-orange) 100%);
  }
  .headline {
    position: absolute;
    left: 0;
    right: 0;
    top: 118px;
    margin: 0;
    text-align: center;
    font-family: "Abril Fatface", serif;
    font-weight: 400;
    line-height: 1;
  }
  .headline-be {
    display: block;
    font-size: 112px;
    color: var(--be-gold);
    text-shadow: 4px 4px 0 var(--ink-shadow);
    letter-spacing: 1px;
    margin-left: -10px;
  }
  .headline-colorful {
    display: block;
    margin-top: 4px;
    font-size: 84px;
    text-shadow: 3px 3px 0 var(--ink-shadow);
    letter-spacing: 1px;
  }
  .c1 { color: var(--col-olive); }
  .c2 { color: var(--col-blush); }
  .c3 { color: var(--col-terracotta); }
  .c4 { color: var(--col-stone); }
  .c5 { color: var(--col-olive); }
  .c6 { color: var(--col-slate); }
</style>
</head>
<body>
  <main class="art-wall">
    <div class="watercolor-bursts" role="img" aria-label="Repeating pattern of hand-painted watercolor bursts in orange, red, blue, violet, green and pink surrounding a white center"></div>
    <h1 class="headline">
      <span class="headline-be">Be</span>
      <span class="headline-colorful"><span class="c1">C</span><span class="c2">o</span><span class="c3">l</span><span class="c4">o</span><span class="c5">r</span><span class="c6">ful</span></span>
    </h1>
  </main>
</body>
</html>
```